New webdesign for a cable company

We need a new design for Lumo Nett.

There exist a suggestion for the page, were we have attached files to show you this. The design here is not good enough, but here you can se what content we need.

You can feel free to give adjustment to this design to make it better, our blow us away with a new brilliant design, but from this design you see what content we need.

The important is that the company get a design who represent its products:
- TV = Cable TV
- Bredbånd = Broadband
- Mobil = Mobile phone
- Strøm = Electricity
- Alarm = Alarm
- Lumo Samlet = a cobain pagage of all our products.

Lumo Nett would like costumers who visit the site to het the impression that Lumo Nett is a professional, innovative and fun company.
Updates

We have to day uploaded pictures of the existing page as the link haven't been working for the most of you as it's placed on a server our developer are using and is often shut it down. 

We have also updated the brief with some new and updated description so please read true the updated brief. 

We will at the same time inform that we haven't been able to give feedback on any of the received design and are sorry for that, we will within the next 24 hours hopefully have started responded the different received designs.

Looking forward to see more suggestion and hope you will help us create and very professional and informative design. 

Reason: We have decided to extend the deadline due to the number of design suggestion who is sent in and your lack of response to all designers due to our own workload.

This project was unfortunately for different reason put on ice for a while, but we are now ready to complete the design and will answer and give feedback too all the received design suggestions. 

Within a couple of days we hope we have answered all you who sent us suggestions, we appreciate all suggestions and hope to get in more suggestions.

Reason: Deisgn description have been updated

Target Market(s)

Our costumer are both private and companies

Industry/Entity Type

Tv

Requirements
Must have
• A easy way to promote and inform about changes in our products, there are a constant change in our products and it must bee a easy and good way to changes ass the marked change. Cheek out this link, for a example of what we like/think of here, https://kabel.fjordvisjon.no

On all pages there must be a easy way to click on a order button and too inform about your interest (thats two different things), could be placed in the top right corner for example. In the order form you should follow a step by step part:
1. Cheek what product we can provide you.
2. Chooce products.
3. Costumer inforamtion.
4. Confirmation.

Somewere on the portal it must be possible for costumers to log on to their own administration, where they can cheek for invoices, other statuses, etc.

A main menu existing of:
Hjem (Home)
Produkter (Products)
Storkunde (key account/large costumers)
Kundeservice (Costumerservice)
Min side (My page)

The main menu should have the following sub titles:
- Under "Produkter"/products our different products must be listed
- Under "Kundeservice"/Costumerservice it must have these submenus:
- Hjelp og støtte = Help.
- Faktura = Invoice
- Brukerguider = Userguides
- Abbonementavtaler = Terms and conditions.

A bottom menu where we have 5 main categories, with sub categories:
Om oss (about us)
- Om Lumo Nett (about Lumo Nett)
- Kontaktinformajson ( contact information)
- Pressemeldinger (Pressrelese)
- Ledige stillinger (positions available)
- KRAB ( and organisastion in our field)

Produkter (Product)
- TV (TV)
- Bredbånd (Broadand)
- Telefoni (telephony, both mobil)
- Strøm (elecricity)
- Arlam (Alarm)

Borrettslag/Sameier (Housing cooperatives)
- Løsninger (solutions)
- Produkter (product)
- Kontaktpersoner (contactpersons)

Utbygger (developer)
- Hva vi kan gjøre for dere. (What we can do for you)

Opperatørnett (operators)

Build up the categories and bottom menu something like this:
https://kabel.fjordvisjon.no
www.brenvik.com
Nice to have
• A main menu existing of:
Hjem (Home)
Produkter (Products)
Lumo Nett
Kontakt oss (Contact us)

Under "Produkter"/products our different products must be listed and under "Kundeservice"/Costumerservice it must have these submenus:
- Hjelp og støtte = Help.
- Faktura = Invoice
Should not have
• Any translation section since the homepage only will be in Norwegian.

```html
<!DOCTYPE html>
<html lang="no">
<head>
<meta charset="utf-8">
<title>Lumo Nett – Client Login/Sign Up</title>
<link href="https://fonts.googleapis.com/css2?family=Carlito:wght@400;700&family=Arimo:wght@400&display=swap" rel="stylesheet">
<style>
:root{
  --orange:#f56a00;
  --orange-light:#ff8a1f;
  --blue:#0d58c8;
  --blue-dark:#0a4bb4;
  --blue-light:#1f7be0;
  --text:#222;
  --panel:#e8ecf0;
  --panel-border:#c9ced4;
  --footer:#4a4a4a;
  --footer-box:#666;
  --footer-line:#6a6a6a;
  --footer-text:#f0f0f0;
  --muted:#d0d0d0;
}
*{margin:0;padding:0;box-sizing:border-box}
html,body{width:1180px;height:1200px;overflow:hidden}
body{position:relative;background:#fff;font-family:"Carlito",sans-serif;color:var(--text)}
.abs{position:absolute}
.header{left:0;top:0;width:1180px;height:127px;background:linear-gradient(#ececec,#fff 45px)}
.brand{left:120px;top:48px;display:flex;align-items:center;gap:10px}
.brand-dot{width:26px;height:26px;border-radius:50%;background:var(--blue)}
.brand-name{font-size:34px;color:var(--blue-dark)}
.nav{left:404px;top:64px;display:flex;gap:19px;font-size:17px}
.top-btn{top:25px;height:25px;background:var(--orange);color:#fff;font-size:16px;line-height:25px;padding:0 9px;box-shadow:1px 1px 2px rgba(0,0,0,.3)}
.phone-top{left:918px;top:60px;display:flex;align-items:center;gap:6px;font-size:23px;color:#555}
.hero{left:0;top:127px;width:1180px;height:366px;background:linear-gradient(var(--blue-dark),var(--blue) 50%,var(--blue-light))}
.hero h1{position:absolute;left:131px;top:28px;font-weight:400;font-size:52px;color:#fff;text-shadow:2px 2px 3px rgba(0,0,0,.45)}
.content{left:119px;top:232px;width:947px;height:642px;background:#fff;box-shadow:0 0 3px rgba(0,0,0,.2)}
.content h2{position:absolute;left:50px;top:48px;font-size:44px;color:var(--orange);text-shadow:1px 1px 2px rgba(0,0,0,.2)}
.panel{position:absolute;top:130px;background:var(--panel);border:1px solid var(--panel-border);border-radius:5px;box-shadow:2px 2px 3px rgba(0,0,0,.2);height:441px}
.form{left:50px;width:537px}
.info{left:598px;width:306px}
.field{position:absolute;left:0;width:180px;text-align:right;font-size:17px}
.input{position:absolute;left:182px;width:238px;height:26px;background:#fff;border:1px solid #b5b5b5}
.check{position:absolute;display:flex;align-items:center;gap:4px;font-size:14px;color:#555}
.box{width:15px;height:15px;background:#fff;border:1px solid #999;position:relative}
.box svg{position:absolute;left:1px;top:-6px}
.signup{position:absolute;left:182px;top:366px;width:137px;height:38px;background:linear-gradient(var(--orange-light),var(--orange));color:#fff;font-size:23px;line-height:38px;padding-left:14px;border-radius:2px;box-shadow:1px 1px 3px rgba(0,0,0,.3)}
.info h3{position:absolute;left:9px;font-weight:400;font-size:23px;color:#333}
.rule{position:absolute;left:9px;width:285px;height:1px;background:#fff;border-top:1px solid #d5d9dd}
.info .big{position:absolute;left:9px;top:72px;font-size:35px;color:var(--blue)}
.info .hours{position:absolute;left:9px;top:114px;font-size:14px}
.info a{position:absolute;left:9px;top:194px;font-size:23px;color:var(--blue)}
.footer{left:0;top:873px;width:1180px;height:327px;background:var(--footer);color:var(--footer-text)}
.footer h4{position:absolute;font-weight:400;font-size:22px;color:#fff}
.fline{position:absolute;height:1px;background:var(--footer-line)}
.contact-row{position:absolute;left:135px;display:flex;gap:10px;font-size:14px;line-height:18px}
.stream{position:absolute;left:427px;top:66px;width:331px;height:192px;background:var(--footer-box);font-family:"Arimo",sans-serif;font-size:10.5px}
.tweet{position:absolute;left:20px;width:296px;color:#eee}
.tweet .date{text-align:right;margin-top:4px;padding-right:15px}
.tsep{position:absolute;left:20px;width:296px;height:1px;background:#555}
.sub-label{position:absolute;font-family:"Arimo",sans-serif;font-size:12px}
.sub-input{position:absolute;left:869px;width:186px;height:28px;background:var(--footer-box)}
.sub-btn{position:absolute;left:869px;top:181px;background:var(--orange);color:#fff;font-size:17px;padding:0 10px;height:28px;line-height:28px;border:1px solid #ff9a4a}
.copy{position:absolute;top:306px;font-family:"Arimo",sans-serif;font-size:12px;color:var(--muted)}
</style>
</head>
<body>
<header class="abs header">
  <div class="abs brand"><span class="brand-dot"></span><span class="brand-name">Lumo Nett</span></div>
  <nav class="abs nav"><span>Hjem</span><span>Produkter</span><span>Kundeservice</span><span>Om oss</span><span>Kontakt oss</span></nav>
  <span class="abs top-btn" style="left:814px">Logout</span>
  <span class="abs top-btn" style="left:893px">Client Login/Sign Up</span>
  <div class="abs phone-top">
    <svg width="13" height="24" viewBox="0 0 13 24"><path d="M4 1c2 0 3 1 3 3l-1 3c0 1-2 1-2 2 0 3 1 7 3 9 1 0 2-1 3 0l2 3c0 2-2 3-4 3C3 22 0 14 0 7 0 3 2 1 4 1z" fill="#f56a00"/></svg>
    <span>47 12 38 90</span>
  </div>
</header>

<section class="abs hero"><h1>Client Login/Sign Up</h1></section>

<main class="abs content">
  <h2>Sign Up Now</h2>
  <div class="panel form">
    <span class="field" style="top:75px">Email Address:</span><span class="input" style="top:71px"></span>
    <span class="field" style="top:123px">Password:</span><span class="input" style="top:119px"></span>
    <span class="field" style="top:170px">Confirm Password:</span><span class="input" style="top:166px"></span>
    <span class="field" style="top:218px">Full Name:</span><span class="input" style="top:214px"></span>
    <span class="field" style="top:284px">Gander:</span>
    <span class="check" style="left:184px;top:284px"><span class="box"><svg width="18" height="20" viewBox="0 0 18 20"><path d="M2 12l4 5L16 1" stroke="#111" stroke-width="2" fill="none"/></svg></span>Male</span>
    <span class="check" style="left:283px;top:284px"><span class="box"></span>Female</span>
    <span class="check" style="left:184px;top:322px"><span class="box"><svg width="18" height="20" viewBox="0 0 18 20"><path d="M2 12l4 5L16 1" stroke="#111" stroke-width="2" fill="none"/></svg></span>I agree to terms &amp; conditions</span>
    <span class="signup">Sign Up <svg width="10" height="12" viewBox="0 0 10 12" style="margin-left:22px"><path d="M2 1l5 5-5 5" stroke="#fff" stroke-width="2.5" fill="none"/></svg></span>
  </div>
  <div class="panel info">
    <h3 style="top:33px">Telefon:</h3>
    <span class="rule" style="top:65px"></span>
    <span class="big">47 12 38 90</span>
    <span class="hours">Telefon betjent hverdager 10:00 -15:00</span>
    <h3 style="top:164px;left:7px">E-post:</h3>
    <a href="#">post@lumonett.no</a>
  </div>
</main>

<footer class="abs footer">
  <h4 style="left:134px;top:40px">Kontakt oss</h4>
  <span class="fline" style="left:134px;top:78px;width:242px"></span>
  <div class="contact-row" style="top:96px"><svg width="16" height="20" viewBox="0 0 16 20"><path d="M8 0a7 7 0 0 0-7 7c0 5 7 13 7 13s7-8 7-13a7 7 0 0 0-7-7z" fill="#fff"/><circle cx="8" cy="7" r="2.5" fill="#4a4a4a"/></svg><span style="width:235px">Lorem ipsum dolor sit amet, consectetur adipisicing elit, sed do eiusmod tempor eiusmod tempor</span></div>
  <div class="contact-row" style="top:160px;font-size:13px"><svg width="16" height="20" viewBox="0 0 13 24"><path d="M4 1c2 0 3 1 3 3l-1 3c0 1-2 1-2 2 0 3 1 7 3 9 1 0 2-1 3 0l2 3c0 2-2 3-4 3C3 22 0 14 0 7 0 3 2 1 4 1z" fill="#fff"/></svg><span>47 12 38 90</span></div>
  <div class="contact-row" style="top:197px;font-size:13px"><svg width="20" height="14" viewBox="0 0 20 14"><rect width="20" height="14" fill="#fff"/><path d="M0 0l10 8 10-8" stroke="#4a4a4a" stroke-width="1.5" fill="none"/></svg><span>post@lumonett.no</span></div>

  <h4 style="left:553px;top:44px;font-size:19px">Nyhetsstrøm</h4>
  <svg class="abs" style="left:465px;top:64px" width="40" height="4" viewBox="0 0 40 4"></svg>
  <svg class="abs" style="left:465px;top:50px" width="42" height="17" viewBox="0 0 42 17"><path d="M0 17L42 0 30 17z" fill="#666"/></svg>
  <div class="stream">
    <div class="tweet" style="top:19px">Lorem ipsum dolor sit amet, consectetur adipisicing elit,<br>sed do eiusmod tempor<div class="date">07,May 2013</div></div>
    <span class="tsep" style="top:64px"></span>
    <div class="tweet" style="top:80px">Lorem ipsum dolor sit amet, consectetur adipisicing elit,<br>sed do eiusmod tempor<div class="date">07,May 2013</div></div>
    <span class="tsep" style="top:125px"></span>
    <div class="tweet" style="top:140px">Lorem ipsum dolor sit amet, consectetur adipisicing elit,<br>sed do eiusmod tempor<div class="date">07,May 2013</div></div>
  </div>

  <h4 style="left:824px;top:40px">Subscribe</h4>
  <span class="fline" style="left:824px;top:78px;width:242px"></span>
  <span class="sub-label" style="left:822px;top:101px">Name:</span><span class="sub-input" style="top:93px"></span>
  <span class="sub-label" style="left:824px;top:143px">Email:</span><span class="sub-input" style="top:135px"></span>
  <span class="sub-btn">Subscribe &gt;</span>

  <span class="fline" style="left:120px;top:274px;width:946px;background:#5e5e5e"></span>
  <span class="copy" style="left:163px">@ Copyright 2013 &nbsp;| &nbsp;LumoNett &nbsp; All rights reserved.</span>
</footer>
</body>
</html>
```